E-book named 'Lanterns Over Marrowby: Building Kinder Firms' needs cover

I need a cover for my ebook and also paper back book.
I need a very appealing cover for my ebook. Social enterprise is a company that gives something back to the society as opposed to only make profit.
The society and its people always benefit.
So far the above is the name chosen but I welcome small changes and ideas also a tag line would also be great something like “everything you need to know to sep up a social enterprise and succeed”
I want to write in the cover something to make people buy it. I want the name Social Enterprise in more evidence ...
Target Market(s)
Students, graduates and business minded people who are thinking of set up a social enterprise company and needs guidance
Industry/Entity Type
It Company
Colors
Designer to choose colors to be used in the design.
Look and feel
Each slider illustrates characteristics of the customer's brand and the style your logo design should communicate.

```html
<!DOCTYPE html>
<html lang="en">
<head>
<meta charset="utf-8">
<title>Lanterns Over Marrowby: Building Kinder Firms</title>
<link rel="stylesheet" href="https://fonts.googleapis.com/css2?family=Bebas+Neue&family=Bungee&family=Montserrat:ital,wght@1,300&display=swap">
<style>
  :root {
    --cover-yellow: #ffc400;
    --cover-yellow-light: #ffd23f;
    --title-white: #ffffff;
    --ink-navy: #2c3457;
    --accent-red: #d1151f;
    --line-white: #ffffff;
  }
  html, body {
    margin: 0;
    padding: 0;
    overflow: hidden;
  }
  .cover {
    position: relative;
    width: 848px;
    height: 1200px;
    background: var(--cover-yellow);
    overflow: hidden;
  }
  .cover-frame {
    position: absolute;
    left: 51px;
    top: 51px;
    width: 745px;
    height: 1097px;
    border: 2px solid var(--line-white);
    box-sizing: border-box;
  }
  .title {
    margin: 0;
    font-weight: normal;
  }
  .title span {
    position: absolute;
    left: 0;
    right: 0;
    text-align: center;
    line-height: 1;
    white-space: nowrap;
  }
  .title-line {
    font-family: "Bebas Neue", "Oswald", sans-serif;
    color: var(--title-white);
    font-size: 96px;
    letter-spacing: 1px;
  }
  .title-line--first  { top: 222px; }
  .title-line--second { top: 350px; }
  .title-line--third  { top: 478px; }
  .tagline {
    top: 591px;
    font-family: "Montserrat", sans-serif;
    font-style: italic;
    font-weight: 300;
    font-size: 19px;
    color: var(--ink-navy);
  }
  .subject-line {
    top: 617px;
    font-family: "Bungee", sans-serif;
    font-size: 96px;
    color: var(--ink-navy);
    letter-spacing: 2px;
  }
  .subject-highlight {
    top: 734px;
    font-family: "Bebas Neue", "Oswald", sans-serif;
    font-size: 134px;
    color: var(--accent-red);
    letter-spacing: 2px;
  }
  .peaks-art {
    position: absolute;
    left: 471px;
    top: 927px;
    width: 271px;
    height: 221px;
    background: linear-gradient(to top, var(--cover-yellow-light), var(--cover-yellow));
  }
</style>
</head>
<body>
  <main class="cover">
    <div class="cover-frame"></div>

    <h1 class="title">
      <span class="title-line title-line--first">Lanterns</span>
      <span class="title-line title-line--second">Over Marrowby:</span>
      <span class="title-line title-line--third">Building</span>
      <span class="tagline">everything you need to know</span>
      <span class="subject-line">KINDER</span>
      <span class="subject-highlight">FIRMS</span>
    </h1>

    <div class="peaks-art" role="img" aria-label="Line illustration of mountain peaks"></div>
  </main>
</body>
</html>
```